International Business Consulting Company Website

RK Harbor Advisors is a U.S-based international consulting firm. We combined passion for success in the global business arena with hands-on experience to help foreign companies navigate the entry into U.S. markets and U.S. companies in initiating and expanding exports to foreign markets.

We need a simple 1 page website
Examples of other consultants’ websites:
http://www.brindlemarkgroup.example/#intro
https://www.tpq-advisory.example
http://morivetagroup.example
https://quillstoneadvisors.example

I also need the designer to suggest stock images that are suitable (related to international business, exports).

We want our web design to be bold, yet clean and simple.

Target Market(s)

US companies that export abroad, foreign companies that want to do business int he US/ open a subsidiary in the US.

Industry/Entity Type

Business Consultant

Coding

Coded - Design and coding required

Font styles to use
Sans Serif

Requirements
Must have
• Company logo on top

```html
<!DOCTYPE html>
<html lang="en">
<head>
<meta charset="utf-8">
<title>RK Harbor Advisors</title>
<link rel="stylesheet" href="https://fonts.googleapis.com/css2?family=Noto+Serif:wght@400;700&display=swap">
<style>
:root{
  --navy:#0d3f8f;
  --blue:#1a4f9c;
  --ink:#2a2a2a;
  --muted:#6b6b6b;
  --line:#dcdcdc;
  --paper:#ffffff;
  --mist:#f2f3f5;
  --field:#cfd6de;
}
*{box-sizing:border-box;margin:0;padding:0}
html,body{width:1200px;height:3462px;overflow:hidden}
body{position:relative;font-family:"Noto Serif",Georgia,serif;color:var(--ink);background:var(--paper)}
.abs{position:absolute}
section{position:absolute;left:0;width:1200px;overflow:hidden}

/* hero */
.hero{top:0;height:590px}
.hero-photo{position:absolute;inset:0;background:radial-gradient(ellipse at 50% 30%,#6fb6f0 0%,#2f6fc0 30%,#163a74 60%,#0a1630 100%)}
.hero-photo::after{content:"";position:absolute;left:0;right:0;bottom:0;height:240px;background:linear-gradient(to bottom,rgba(10,20,40,0),rgba(10,18,35,.85))}
.brand{position:absolute;left:100px;top:44px;display:flex;align-items:center;gap:12px;color:#fff}
.brand-square{width:70px;height:74px;border:3px solid currentColor}
.brand-name{font-size:30px;line-height:1;font-weight:400;letter-spacing:1px}
.nav{position:absolute;top:76px;left:490px;display:flex;align-items:center;font-size:12.5px;color:#fff;letter-spacing:.5px}
.nav a{color:#fff;text-decoration:none;margin-right:46px}
.login{position:absolute;left:984px;top:66px;width:116px;height:40px;border:2px solid #fff;border-radius:20px;color:#fff;font-size:12.5px;display:flex;align-items:center;justify-content:center;gap:6px}
.hero-title{position:absolute;top:300px;width:100%;text-align:center;color:#fff;font-size:72px;font-weight:700;line-height:1}
.hero-sub{position:absolute;top:388px;width:100%;text-align:center;color:#fff;font-size:21px;letter-spacing:12px;font-weight:700}
.scroll-cue{position:absolute;left:582px;top:500px;width:36px;height:58px;border:2px solid #fff;border-radius:18px}

/* welcome */
.welcome{top:590px;height:368px;text-align:center}
.welcome h1{position:absolute;top:72px;width:100%;font-size:42px;font-weight:700}
.welcome h2{position:absolute;top:138px;width:100%;font-size:24px;font-weight:700;letter-spacing:5px;color:var(--blue)}
.welcome p{position:absolute;top:190px;left:230px;width:740px;font-size:13.5px;line-height:30px;color:var(--muted)}

/* services */
.services{top:958px;height:953px;background:var(--mist)}
.services h2{position:absolute;top:80px;width:100%;text-align:center;font-size:35px;font-weight:400}
.photo{position:absolute;border:4px solid #fff;box-shadow:0 1px 4px rgba(0,0,0,.15)}
.photo-exports{left:104px;top:180px;width:364px;height:332px;background:linear-gradient(135deg,#d7dde4,#6e8fb6 55%,#2a4f7f)}
.photo-fdi{left:732px;top:538px;width:364px;height:330px;background:linear-gradient(135deg,#f4f4f4,#dcdcdc 50%,#8b8b8b)}
.service-title{position:absolute;font-size:20px;line-height:34px;font-weight:400}
.service-title u{color:var(--blue)}
.checklist{position:absolute;list-style:none;font-size:12px;line-height:30.5px;color:var(--muted)}
.checklist li{position:relative;padding-left:28px}
.checklist li::before{content:"";position:absolute;left:2px;top:11px;width:9px;height:9px;border:2px solid var(--blue);border-radius:50%}

/* team */
.team{top:1911px;height:466px}
.portrait{position:absolute;left:108px;top:85px;width:296px;height:296px;border-radius:50%;border:4px solid #fff;box-shadow:0 0 0 2px #d0d0d0;overflow:hidden;background:radial-gradient(circle at 50% 40%,#6a5043,#2a201c 70%)}
.portrait-label{position:absolute;left:0;right:0;bottom:0;height:66px;background:var(--navy);color:#fff;text-align:center;padding-top:8px}
.portrait-label b{display:block;font-size:14px;letter-spacing:.5px}
.portrait-label span{font-size:13px}
.team h2{position:absolute;left:446px;top:100px;font-size:30px;font-weight:400}
.team p{position:absolute;left:446px;top:152px;width:654px;font-size:12px;line-height:30px;color:var(--muted)}
.team p a{color:var(--blue);text-decoration:none}
.social-squares{position:absolute;left:446px;top:322px;display:flex;gap:4px}
.social-squares span{width:36px;height:36px}
.read-more{position:absolute;left:1014px;top:331px;font-size:12px;color:var(--blue);text-decoration:underline}

/* contact */
.contact{top:2377px;height:568px;background:linear-gradient(to bottom,#3b4c73 0%,#57708f 35%,#1f5f7d 60%,#0e4e6e 80%,#0a3550 100%)}
.contact-card{position:absolute;left:247px;top:76px;width:706px;height:416px;background:#fff}
.contact-card h2{position:absolute;top:52px;width:100%;text-align:center;font-size:28px;font-weight:400;letter-spacing:3px}
.field{position:absolute;border:1px solid var(--line);font-size:11px;color:#8a8a8a;padding:12px 14px}
.send{position:absolute;left:39px;top:318px;width:626px;height:44px;background:var(--navy);color:#fff;font-size:13px;display:flex;align-items:center;justify-content:center}

/* footer */
.footer{top:2945px;height:517px}
.footer-brand{position:absolute;left:115px;top:82px;display:flex;align-items:center;gap:12px;color:var(--navy)}
.footer-brand .brand-square{width:76px;height:80px}
.footer-brand .brand-name{font-size:30px}
.contact-list{position:absolute;left:113px;top:204px;list-style:none;font-size:12px;color:var(--muted)}
.contact-list li{position:relative;padding-left:35px;line-height:23px;margin-bottom:14px}
.contact-list svg{position:absolute;left:0;top:4px}
.footer h3{position:absolute;top:88px;font-size:20px;font-weight:400;letter-spacing:1px}
.newsletter-text{position:absolute;left:478px;top:122px;width:300px;font-size:12px;line-height:28px;color:var(--muted)}
.newsletter-input{position:absolute;left:478px;top:189px;width:357px;height:51px;border:1px solid var(--line);font-size:11px;color:#8a8a8a;padding:17px 14px}
.subscribe{position:absolute;left:478px;top:247px;width:143px;height:48px;background:var(--navy);color:#fff;font-size:13px;display:flex;align-items:center;justify-content:center}
.follow{position:absolute;left:912px;top:148px;display:flex;gap:8px}
.follow span{width:38px;height:38px;border-radius:50%;border:2px solid}
.rule{position:absolute;left:100px;right:100px;top:425px;border-top:1px solid var(--line)}
.copyright{position:absolute;top:460px;width:100%;text-align:center;font-size:12px;color:var(--muted)}
</style>
</head>
<body>

<section class="hero">
  <div class="hero-photo" role="img" aria-label="Silhouetted business people at a boardroom table before a glowing world map and city skyline"></div>
  <div class="brand"><div class="brand-square"></div><div class="brand-name">RK Harbor Advisors</div></div>
  <nav class="nav"><a>HOME</a><a>ABOUT US</a><a>SERVICES</a><a>BLOG</a><a>CONTACT US</a></nav>
  <div class="login">
    <svg width="11" height="13" viewBox="0 0 11 13"><rect x="1" y="5.5" width="9" height="7" fill="#fff"/><path d="M3 5.5V3.5a2.5 2.5 0 0 1 5 0v2" fill="none" stroke="#fff" stroke-width="1.5"/></svg>
    LOG IN
  </div>
  <div class="hero-title">RK HARBOR</div>
  <div class="hero-sub">ADVISORS</div>
  <div class="scroll-cue">
    <svg width="32" height="54" viewBox="0 0 32 54"><path d="M16 40V16M10 22l6-6 6 6" fill="none" stroke="#fff" stroke-width="2.5"/></svg>
  </div>
</section>

<section class="welcome">
  <h1>WELCOME TO</h1>
  <h2>RK HARBOR ADVISORS</h2>
  <p>RK Harbor Advisors is a U.S-based international consulting firm. We combined passion for success in the global business arena with hands-on experience to help foreign companies navigate the entry into U.S. markets and U.S. companies in initiating and expanding exports to foreign markets.</p>
</section>

<section class="services">
  <h2>OUR SERVICES</h2>
  <div class="photo photo-exports" role="img" aria-label="Business team gathered around a table with a digital globe display"></div>
  <div class="service-title" style="left:498px;top:206px"><u>Exports</u> assists U.S. companies with their export initiatives by</div>
  <ul class="checklist" style="left:498px;top:248px;width:600px">
    <li>Identifying and developing new customer relationships in foreign markets</li>
    <li>Organizing trade mission trips</li>
    <li>Coordinating successful trade show visits</li>
    <li>Providing an assistance with the completion of a strategic export plan</li>
    <li>Finding additional resources to support and grow companies' exports</li>
    <li>Connecting companies with other international trade experts to further support their international logistics, payment &amp; financing management, and to address any trade regulations and legal issues</li>
  </ul>
  <div class="service-title" style="left:104px;top:584px;width:620px"><u>FDI</u> assists international companies with navigating the entry into U.S. markets by</div>
  <ul class="checklist" style="left:104px;top:666px;width:560px">
    <li>Managing the site selection process</li>
    <li>Collecting market data</li>
    <li>Site identification and analysis</li>
    <li>Providing an appraisal of proposed incentives and financing assistance</li>
    <li>Management of the documentation process</li>
  </ul>
  <div class="photo photo-fdi" role="img" aria-label="Overhead view of colleagues meeting around a white table with laptops"></div>
</section>

<section class="team">
  <div class="portrait" role="img" aria-label="Portrait of the company president">
    <div class="portrait-label"><b>MARA VELINSKA</b><span>President</span></div>
  </div>
  <h2>ABOUT OUR TEAM</h2>
  <p><a>Mara Velinska</a> has ten years of experience in economic development, foreign direct investment (FDI) and trade. Prior to founding RK Harbor Advisors, she worked as Director of Global Business Development – Europe at the Ridgeview Economic Development Commission (REDC) assisting European companies to expand in Arkansas. While at the REDC, Mara participated in a number of international trade shows and organized multiple investment and trade missions for the state's governors.</p>
  <div class="social-squares"><span style="background:#3b5998"></span><span style="background:#1da1f2"></span><span style="background:#b0183a"></span><span style="background:#d6246e"></span></div>
  <div class="read-more">Read More ›</div>
</section>

<section class="contact">
  <div class="abs" style="inset:0" role="img" aria-label="City skyline at dusk reflected over a harbor with fountains"></div>
  <div class="contact-card">
    <h2>CONTACT FORM</h2>
    <div class="field" style="left:39px;top:113px;width:312px;height:44px">First Name</div>
    <div class="field" style="left:355px;top:113px;width:310px;height:44px">Last Name</div>
    <div class="field" style="left:39px;top:161px;width:312px;height:44px">Email</div>
    <div class="field" style="left:355px;top:161px;width:310px;height:44px">Phone</div>
    <div class="field" style="left:39px;top:212px;width:626px;height:97px">Message</div>
    <div class="send">SEND MESSAGE</div>
  </div>
</section>

<section class="footer">
  <div class="footer-brand"><div class="brand-square"></div><div class="brand-name">RK Harbor Advisors</div></div>
  <ul class="contact-list">
    <li><svg width="18" height="15" viewBox="0 0 18 15"><path d="M9 1L1 8h2.5v6h4v-4h3v4h4V8H17z" fill="#1a4f9c"/></svg>RK Harbor Advisors, LLC<br>Mara Velinska, MBA<br>President</li>
    <li><svg width="12" height="18" viewBox="0 0 12 18"><rect x="1" y="1" width="10" height="16" rx="2" fill="none" stroke="#1a4f9c" stroke-width="2"/><circle cx="6" cy="14" r="1.2" fill="#1a4f9c"/></svg>Call Us : +1 (555) 014-0288</li>
    <li><svg width="18" height="14" viewBox="0 0 18 14"><rect x="1" y="1" width="16" height="12" fill="none" stroke="#1a4f9c" stroke-width="1.6"/><path d="M1 1l8 7 8-7" fill="none" stroke="#1a4f9c" stroke-width="1.6"/></svg>info@rkharboradvisors.example</li>
  </ul>
  <h3 style="left:478px">SIGN UP NEWSLETTER</h3>
  <p class="newsletter-text">Excepteur sint occaecat cupidatat non proident, sunt in culpa qui officia deserunt mollit</p>
  <div class="newsletter-input">Email..</div>
  <div class="subscribe">SUBSCRIBE</div>
  <h3 style="left:912px">FOLLOW US</h3>
  <div class="follow"><span style="border-color:#3b5998"></span><span style="border-color:#1da1f2"></span><span style="border-color:#1a4f9c"></span><span style="border-color:#c4302b"></span></div>
  <div class="rule"></div>
  <div class="copyright">© copyright 2017 RK Harbor Advisors . All rights reserved</div>
</section>

</body>
</html>
```